Business Card- Can you make it cool vs boring!

Need a refresh on my business card! Want it to be modern but simple, classic and a pop of coolness! we do senior living and it is boring. but that doesn't mean our business card have to look boring! Open to two sided cards. our website is www.Bruvel-HQ.com

Target Market(s)

capital market

Industry/Entity Type

senior housing/ real estate

Contact Information for Business Card

logo/ name/ cell/ address/ www.Bruvel-HQ.com/ space for a QR code

Requirements
Must have
• maybe a QR code (do not make prominent I may not use the QR so design where it can be taken out) that link to more about us/ landing page. needs to be modern but clean
Should not have
• clip art or script

```html
<!DOCTYPE html>
<html lang="en">
<head>
<meta charset="utf-8">
<title>Bruvel Living – Business Card</title>
<link href="https://fonts.googleapis.com/css2?family=Saira:wght@400;500&display=swap" rel="stylesheet">
<style>
  :root {
    --rust: #ad4f26;
    --slate: #7b7b7b;
    --paper: #ffffff;
    --backdrop: #e6e6e6;
    --rule-tone: #d9d9d9;
  }
  * { margin: 0; padding: 0; box-sizing: border-box; }
  html, body {
    width: 1200px;
    height: 1200px;
    overflow: hidden;
    background: var(--backdrop);
    font-family: "Saira", Arial, sans-serif;
  }
  .card {
    position: absolute;
    left: 159px;
    width: 881px;
    height: 516px;
    background: var(--paper);
    overflow: hidden;
  }
  .card--front { top: 61px; }
  .card--back { top: 607px; height: 514px; }

  .brand-name {
    position: absolute;
    left: 0;
    width: 100%;
    text-align: center;
    color: var(--rust);
    font-weight: 500;
    font-size: 72px;
    letter-spacing: 12px;
    line-height: 1;
    padding-left: 12px;
    white-space: nowrap;
  }
  .card--front .brand-name { top: 214px; z-index: 2; }
  .card--back .brand-name { top: 172px; }

  .contact-band {
    position: absolute;
    left: 0;
    top: 248px;
    width: 100%;
    height: 183px;
    background: var(--rust);
  }
  .band-notch {
    position: absolute;
    left: 100px;
    top: 248px;
    width: 681px;
    height: 46px;
    background: var(--paper);
    border-radius: 0 0 18px 18px;
  }
  .contact-item {
    position: absolute;
    top: 352px;
    display: flex;
    align-items: flex-start;
    gap: 16px;
    color: var(--paper);
    font-size: 21px;
    line-height: 29px;
    letter-spacing: 0.3px;
  }
  .contact-item--phone { left: 61px; }
  .contact-item--address { left: 451px; }
  .contact-item address { font-style: normal; }
  .contact-icon {
    width: 26px;
    height: 26px;
    flex: none;
    margin-top: 1px;
  }
  .website {
    position: absolute;
    top: 450px;
    width: 100%;
    text-align: center;
    color: var(--slate);
    font-size: 21px;
    letter-spacing: 2.5px;
  }
  .skyline-area {
    position: absolute;
    left: 0;
    top: 422px;
    width: 100%;
    height: 40px;
    background: var(--rule-tone);
  }
</style>
</head>
<body>

<section class="card card--front">
  <div class="contact-band"></div>
  <div class="band-notch"></div>
  <h1 class="brand-name">BRUVEL LIVING</h1>

  <div class="contact-item contact-item--phone">
    <svg class="contact-icon" viewBox="0 0 26 26" aria-hidden="true">
      <rect width="26" height="26" rx="4" fill="#fff"/>
      <path d="M8.2 6.5c.5-.4 1.2-.3 1.5.2l1.5 2.4c.3.5.2 1.1-.2 1.5l-1 .9c.8 1.8 2.2 3.3 4 4.2l.9-1c.4-.4 1-.5 1.5-.2l2.4 1.5c.5.3.6 1 .2 1.5l-1.1 1.3c-.6.7-1.6.9-2.5.6-4-1.5-7-4.6-8.4-8.6-.3-.9-.1-1.9.6-2.5z" fill="var(--rust)"/>
    </svg>
    <span>(555) 214-0387</span>
  </div>

  <div class="contact-item contact-item--address">
    <svg class="contact-icon" viewBox="0 0 26 26" aria-hidden="true">
      <rect width="26" height="26" rx="4" fill="#fff"/>
      <path d="M13 5.5c-3 0-5.3 2.3-5.3 5.2 0 3.8 5.3 9.6 5.3 9.6s5.3-5.8 5.3-9.6c0-2.9-2.3-5.2-5.3-5.2zm0 7.2a2 2 0 1 1 0-4 2 2 0 0 1 0 4z" fill="var(--rust)"/>
    </svg>
    <address>480 Cedar Mill Lane, Suite #210<br>Oakridge Falls, TX 77001</address>
  </div>

  <p class="website">www.Bruvel-HQ.com</p>
</section>

<section class="card card--back">
  <h2 class="brand-name">BRUVEL LIVING</h2>
  <div class="skyline-area" role="img" aria-label="Thin grey skyline line illustration running across the card"></div>
</section>

</body>
</html>
```